Business Card Design

We need a design for business cards for our company. We have a logo. We teach EMT's and we are based out of Virginia. The information that will need to add would be, name, title, phone number, email, address. On the back of the business card would be "Trained today, ready tomorrow"

Target Market(s)

People that want to become EMT's

Colors

Designer to choose colors to be used in the design.

Requirements
Must have
• company logo

```html
<!DOCTYPE html>
<html lang="en">
<head>
<meta charset="utf-8">
<title>Rescue Ready Academy – Business Card</title>
<link href="https://fonts.googleapis.com/css2?family=Montserrat:wght@400;500;700;800&display=swap" rel="stylesheet">
<style>
  :root {
    --stage: #2b2e33;
    --navy: #1f2a35;
    --red: #c51f32;
    --white: #ffffff;
    --grey: #555b61;
    --rule: #9a9ea3;
  }
  * { box-sizing: border-box; margin: 0; padding: 0; }
  html, body { width: 1200px; height: 900px; overflow: hidden; }
  body {
    background: var(--stage);
    font-family: "Montserrat", Arial, sans-serif;
    position: relative;
  }
  .card {
    position: absolute;
    left: 280px;
    width: 640px;
    height: 366px;
    overflow: hidden;
    border-radius: 3px;
    box-shadow: 0 14px 30px rgba(0,0,0,.45);
  }
  .card--front { top: 60px; background: var(--white); }
  .card--back { top: 474px; background: var(--navy); }

  .front__brand {
    position: absolute; left: 0; top: 0;
    width: 100%; height: 150px;
    background: var(--navy);
    display: flex; align-items: center; justify-content: center;
  }
  .wordmark {
    display: flex; align-items: center; gap: 12px;
  }
  .wordmark__dot {
    width: 14px; height: 14px; border-radius: 50%;
    background: var(--red);
    flex: none;
  }
  .wordmark__name {
    color: var(--red);
    font-weight: 800;
    font-size: 30px;
    letter-spacing: 0.5px;
    line-height: 1.05;
    text-transform: uppercase;
  }

  .person {
    position: absolute; left: 44px; top: 178px;
  }
  .person__name {
    color: var(--red); font-weight: 700; font-size: 20px;
    letter-spacing: 0.5px; text-transform: uppercase;
  }
  .person__title {
    color: var(--grey); font-size: 14px; margin-top: 2px;
  }
  .front__rule {
    position: absolute; left: 44px; right: 44px; top: 250px;
    height: 1px; background: var(--rule);
  }
  .contact {
    position: absolute; right: 44px; top: 266px;
    list-style: none; text-align: right;
  }
  .contact__item {
    display: flex; align-items: center; justify-content: flex-end;
    gap: 10px; color: var(--grey); font-size: 16px; line-height: 32px;
  }
  .contact__icon { width: 18px; height: 18px; flex: none; }

  .back__brand {
    position: absolute; left: 0; top: 0; width: 100%; height: 250px;
    display: flex; align-items: center; justify-content: center;
  }
  .back__band {
    position: absolute; left: 0; bottom: 0; width: 100%; height: 116px;
    background: var(--red);
    display: flex; align-items: center; justify-content: center;
  }
  .tagline {
    color: var(--white); font-weight: 700; font-size: 18px;
    letter-spacing: 3px; text-transform: uppercase;
  }
</style>
</head>
<body>
  <section class="card card--front" aria-label="Business card front">
    <div class="front__brand">
      <div class="wordmark">
        <span class="wordmark__dot"></span>
        <span class="wordmark__name">Rescue Ready<br>Academy</span>
      </div>
    </div>
    <div class="person">
      <p class="person__name">Corin Vastel</p>
      <p class="person__title">Sales Manager</p>
    </div>
    <div class="front__rule"></div>
    <ul class="contact">
      <li class="contact__item">555-210-4476
        <svg class="contact__icon" viewBox="0 0 24 24" fill="none" stroke="#c51f32" stroke-width="2">
          <circle cx="12" cy="12" r="10"/>
          <path d="M8.5 7.5l2 2-1.2 1.5a7 7 0 0 0 3.7 3.7l1.5-1.2 2 2-1.3 1.5c-4 0-8.5-4.5-8.5-8.5z" fill="#c51f32" stroke="none"/>
        </svg>
      </li>
      <li class="contact__item">info@rescuereadyacademy.com
        <svg class="contact__icon" viewBox="0 0 24 24" fill="none" stroke="#c51f32" stroke-width="2">
          <rect x="3" y="5" width="18" height="14"/>
          <path d="M3 5l9 8 9-8"/>
        </svg>
      </li>
    </ul>
  </section>

  <section class="card card--back" aria-label="Business card back">
    <div class="back__brand">
      <div class="wordmark">
        <span class="wordmark__dot"></span>
        <span class="wordmark__name">Rescue Ready<br>Academy</span>
      </div>
    </div>
    <div class="back__band">
      <p class="tagline">Trained today, ready tomorrow</p>
    </div>
  </section>
</body>
</html>
```